依頼詳細
店頭を飾る新商品POPを作成していただきたいです。これから目玉となる商品ですので、少し高級感のある目を引くデザインを希望いたします。
記載項目
新発売・デニッシュたい焼き・外はサクサク中はもっちり新食感たい焼き・180円・商品画像(データ添付します)・店舗ロゴ(データ添付します)・イメージキャラ(データ添付します)
サイズ
A1
ページ数
片面
希望イメージ
シンプル 複雑
単色 カラフル
暗い 明るい
日常 高級
遊び心 厳粛
未来的 伝統的
女性的 男性的
希望する色
赤 黒 茶色・ゴールド
納品ファイル
• 高解像度JPG (.jpg)
• イラストレーター形式 (.ai)
• フォトショップ形式 (.psd)
補足説明
A1サイズのデータ確認後、A3/ショウカードサイズにリサイズしたデータも希望します。
イメージがわきやすいよう店舗画像も添付します。
データ追加
ロゴのデータが不足していたようなので追加します。添付した店舗写真以外はポスターに入れ込んでほしいです。
よろしくお願いいたします。
何点か作品を拝見させていただきました。
タイトルのデニッシュたい焼きの文字は筆文字で大きくを希望いたします。

文字の参考画像です。
たくさんのご提案ありがとうございます。
鯛焼きにしては価格が高めの設定なのでもう少し高級感のあるデザインを希望いたします。
黒を基調とした光沢感のあるような、、
宜しくお願い致します。
■ 選んだ理由

クライアントが気に入ったため

■ 提案者全員のお礼・コメント

いつもありがとうございます。
またよろしくお願いいたします。

```html
<!DOCTYPE html>
<html lang="ja">
<head>
<meta charset="utf-8">
<title>デニッシュたい焼き 新発売</title>
<link href="https://fonts.googleapis.com/css2?family=Yuji+Boku&family=Yuji+Syuku&family=Zen+Kaku+Gothic+New:wght@700;900&display=swap" rel="stylesheet">
<style>
  :root {
    --ink: #0d0c0c;
    --ink-soft: #2a2726;
    --pattern: #3a3634;
    --white: #ffffff;
    --red: #c8151b;
    --red-deep: #9c0c10;
    --gold: #e7c66b;
    --bake-light: #c88a4a;
    --bake-mid: #8a4f22;
    --bake-dark: #4a2610;
  }
  * { margin: 0; padding: 0; box-sizing: border-box; }
  html, body { width: 849px; height: 1200px; overflow: hidden; background: var(--ink); }
  .poster {
    position: relative;
    width: 849px; height: 1200px;
    overflow: hidden;
    background: radial-gradient(ellipse at 60% 30%, var(--ink-soft) 0%, var(--ink) 70%);
  }
  .pattern-field {
    position: absolute; inset: 0;
    background: radial-gradient(circle at 30% 20%, var(--pattern) 0%, transparent 55%),
                radial-gradient(circle at 85% 55%, var(--pattern) 0%, transparent 45%);
    opacity: .55;
  }
  .vertical { writing-mode: vertical-rl; position: absolute; color: var(--white); white-space: nowrap; }
  .tagline {
    top: 40px; left: 150px;
    font-family: "Yuji Syuku", serif;
    font-size: 36px; line-height: 1.45; letter-spacing: 2px;
  }
  .title-line {
    font-family: "Yuji Boku", serif;
    font-weight: 400;
    text-shadow: 0 0 14px rgba(0,0,0,.7);
    line-height: 1;
  }
  .title-denish { top: 55px; left: 535px; font-size: 104px; letter-spacing: -2px; }
  .title-taiyaki { top: 130px; left: 335px; font-size: 180px; letter-spacing: -6px; }
  .brand-vertical {
    top: 270px; left: 668px;
    font-family: "Yuji Syuku", serif;
    font-size: 38px; letter-spacing: 2px; line-height: 1;
  }
  .brand-dot {
    position: absolute; top: 400px; left: 679px;
    width: 16px; height: 16px; background: var(--red);
  }
  .product-photo { position: absolute; left: 0; top: 380px; width: 849px; height: 820px; }
  .badge-new {
    position: absolute; top: 900px; left: 652px;
    width: 175px; height: 84px;
    background: linear-gradient(var(--red), var(--red-deep));
    border: 4px solid var(--gold); border-radius: 18px;
    color: var(--white);
    font-family: "Zen Kaku Gothic New", sans-serif; font-weight: 900;
    font-size: 42px; display: flex; align-items: center; justify-content: center;
  }
  .price-tag {
    position: absolute; right: 0; bottom: 0;
    width: 215px; height: 82px;
    background: var(--red);
    border-top-left-radius: 16px;
    color: var(--white);
    font-family: "Zen Kaku Gothic New", sans-serif; font-weight: 900;
    display: flex; align-items: baseline; justify-content: center; padding-top: 10px;
  }
  .price-unit { font-size: 28px; margin-right: 6px; }
  .price-amount { font-size: 56px; letter-spacing: -1px; }
  .price-yen { font-size: 30px; }
  .mascot {
    position: absolute; left: 12px; bottom: 28px;
    width: 100px; height: 120px; border-radius: 50% 50% 40% 40%;
    background: linear-gradient(#d9d6e6, #5a5f8a);
  }
  .brand-footer {
    position: absolute; left: 124px; bottom: 36px;
    font-family: "Yuji Syuku", serif;
    font-size: 50px; color: var(--white); letter-spacing: 2px; line-height: 1;
  }
</style>
</head>
<body>
<main class="poster">
  <div class="pattern-field" role="img" aria-label="黒地に浮かぶ淡い和柄の花文様"></div>

  <svg class="product-photo" viewBox="0 0 849 820" role="img" aria-label="こんがり焼けたデニッシュたい焼きの商品写真">
    <defs>
      <linearGradient id="bake" x1="0" y1="0" x2="1" y2="1">
        <stop offset="0" stop-color="#c88a4a"/>
        <stop offset=".5" stop-color="#8a4f22"/>
        <stop offset="1" stop-color="#4a2610"/>
      </linearGradient>
    </defs>
    <path d="M-40 380 C 80 170, 330 110, 560 140 C 700 160, 800 120, 880 60 L 880 300 C 820 330, 760 420, 700 520 C 600 700, 300 800, 60 820 L -40 820 Z" fill="url(#bake)"/>
  </svg>

  <p class="vertical tagline">外はサクサク<br>中はもっちり<br>新食感たい焼き</p>

  <h1>
    <span class="vertical title-line title-denish">デニッシュ</span>
    <span class="vertical title-line title-taiyaki">たい焼き</span>
  </h1>

  <span class="vertical brand-vertical">麦穂堂</span>
  <span class="brand-dot"></span>

  <div class="badge-new">新発売</div>

  <div class="mascot" role="img" aria-label="お店のイメージキャラクター"></div>
  <span class="brand-footer">麦穂堂</span>

  <div class="price-tag">
    <span class="price-unit">1個</span><span class="price-amount">180</span><span class="price-yen">円</span>
  </div>
</main>
</body>
</html>
```